Larkfield Rowhomes - Billboard design for our newly renovated townhome community

We have a 5' wide x 4' tall billboard at the entrance to our apartment community, that needs to have the acrylic insert replaced. It is a 2 sided sign, and we are planning to use the same image on both sides. We are called Larkfield Rowhomes, and have 48 townhomes that are all 2 bedroom, 1 1/2 bath. A few things we would like to get across on the signage: "Newly Renovated" "2 bed 1 1/2 bath" "Full size W/D in every home" " New Appliances" I've included our parent company's logo - this is the only image I could think of, but it might not be worth having it on the sign. We are in Colorado, so mountain theme could be nice and also sunshine/sun since we are called "Larkfield"

Industry/Entity Type

Apartment

Font styles to use
Sans Serif

Requirements
Must have
• Newly Renovated
2 bed 1 1/2 bath
Full size W/D in every home
Virtual Tours available
www.brambletonhomesco.example
855 - 413 - 9286
Nice to have
• We are located in Colorado - possibly mountain theme? Since our community is called "Larkfield Rowhomes" - anything bright with Sun / Sunshine might look really nice as well.

```html
<!DOCTYPE html>
<html lang="en">
<head>
<meta charset="UTF-8">
<title>Larkfield Rowhomes</title>
<link rel="stylesheet" href="https://fonts.googleapis.com/css2?family=Playfair+Display:wght@700;800&family=Jost:wght@400;600&display=swap">
<style>
  :root {
    --sky-peach: #f9d4a6;
    --sky-cream: #fce3a7;
    --sky-rose: #f5c3a9;
    --ink: #0b0e0b;
    --ridge-orange: #e8772a;
    --ridge-rust: #a83a1e;
    --ridge-brown: #4a1a12;
    --ground: #010d03;
    --footer-text: #ffffff;
  }
  * { margin: 0; padding: 0; box-sizing: border-box; }
  html, body { width: 1200px; height: 962px; overflow: hidden; }
  body { background: var(--ground); }
  .billboard {
    position: relative;
    width: 1200px;
    height: 962px;
    overflow: hidden;
    background:
      radial-gradient(ellipse 420px 300px at 960px 200px, rgba(244,184,166,0.7), transparent 70%),
      radial-gradient(ellipse 520px 360px at 180px 620px, var(--sky-cream), transparent 75%),
      linear-gradient(100deg, var(--sky-peach) 0%, #f9d8a8 45%, var(--sky-rose) 100%);
  }
  .title {
    position: absolute;
    top: 78px;
    left: 0;
    width: 1200px;
    text-align: center;
    font-family: "Playfair Display", "Bodoni Moda", serif;
    font-weight: 700;
    font-size: 150px;
    line-height: 146px;
    color: var(--ink);
    letter-spacing: 1px;
  }
  .features {
    position: absolute;
    top: 410px;
    left: 588px;
    list-style: none;
    font-family: "Jost", sans-serif;
    font-weight: 400;
    font-size: 38px;
    line-height: 47.5px;
    color: var(--ink);
  }
  .features li::before {
    content: "•";
    display: inline-block;
    width: 20px;
    font-size: 28px;
  }
  .landscape {
    position: absolute;
    left: 0;
    top: 680px;
    width: 1200px;
    height: 160px;
    background: linear-gradient(180deg,
      var(--ridge-orange) 0%,
      var(--ridge-rust) 35%,
      var(--ridge-brown) 70%,
      var(--ground) 100%);
  }
  .footer {
    position: absolute;
    left: 0;
    top: 840px;
    width: 1200px;
    height: 122px;
    background: var(--ground);
  }
  .contact {
    position: absolute;
    left: 0;
    top: 870px;
    width: 1200px;
    text-align: center;
    font-family: "Jost", sans-serif;
    font-weight: 600;
    font-size: 33px;
    line-height: 40px;
    color: var(--footer-text);
    letter-spacing: 0.5px;
  }
</style>
</head>
<body>
  <main class="billboard">
    <h1 class="title">Larkfield<br>Rowhomes</h1>
    <ul class="features">
      <li>Newly Renovated</li>
      <li>2 bed 1 1/2 bath</li>
      <li>Full size W/D in every home</li>
      <li>New Appliances</li>
      <li>Virtual Tours available</li>
    </ul>
    <div class="landscape" role="img" aria-label="Illustration of a setting sun over layered orange and brown mountain ridges"></div>
    <div class="footer"></div>
    <p class="contact">WWW.BRAMBLETONHOMESCO.EXAMPLE • 855 - 413 - 9286</p>
  </main>
</body>
</html>
```